We are looking to improve our packaging, because we are wanting to secure our products into five star hotels, spa and wellness centres and maybe even high end retail department stores. That is why it is important it must look the part. We are even prepared to change our current packaging (White stand up pouches) for something different e.g box etc...

Please keep in mind when designing our new Serenwell packaging that our product range will extend to Room Sprays, Candles, Diffuser, Essential Oils, Soaps, Body Scrubs, Milk Baths, Body Lotions, Face Products. So the design will need to compliment and we must be able to adjust the artwork with ease to fit bottles big and small, tubes, boxes glass jars etc... at later stage.

Please see inspiration images of packaging I like. But please do not copy them. We would like something that is unique to our brand that will last for 2-4 years before we have to change the packaging again.

Our current packaging is in a white stand up pouches.
Updates

Project Deadline Extended Reason: Hi All,I have decided to extend the Serenwell Calm Mix Packaging project as the designs I have received are not what I am looking for and are not polished enough for the retail health and spa market. Some of the ideas I received are on the right track, but they need to be reworked a bit more to give our packaging a premium high end looking product. I am trying to get our products into large retail outlets department stores, Chemists, Health and natural product stores, 5 star spa resorts and hotels and eventually export it globally and with so many similar products available for sale our products needs to stand out from the rest of the competition. We use premium grade salts with natural and organic ingredients in our products when we make them. They do not have any harsh chemicals in them. At the moment I am keeping to the stand up white pouches for now, but this will change later this year to a box. We have a good product that sells well, but our current look and feel of our packaging is letting us down and making it difficult to market into the bigger retail stores. I have attached a few sample ideas of what we like, but with our own unique mark to it. We would like something that is unique to us to give our Serenwell brand its own identity. I will leave this up to your creative skills.Our Serenwell product range will branch out to the following in a couple of months. Body Scrubs, Liquid Soaps, Soaps, Body and Face Lotions, Milk baths, Bath and Spa Tea Bags, Bubble Paths, Herbal and Fragranced Bath & Spa products, Steam Therapy, Massage and Bath Oils, Room Sprays, Home Fragrances and Essential oils. So please keep this mind when designing a label that it must be easily adapted to different shapes and size products. e.g. boxes, jars, tubes and bottles.If you have any question before you start, please send me a message.Thank you for taking the time to read our extended brief and very excited to see your designs. Kind Regards, Added Saturday, January 9, 2016

Target Market(s)

Male and female, natural products, well-being, holistic, wellness centres, spa resorts, 5 stars hotels and upmarket.

Industry/Entity Type

Health And Wellness

Font styles to use
Serif
Sans Serif
Other font styles liked:
• Open Sans

Requirements
Must have
• Front: Company Name: Brand name Serenwell Calm Mix (See logo attached or feel fry to add your design flair to this). Please insert Front Packaging copy, 100% pure & natural logo, weight of item 1kg
• Back: Palvex logo (attached), Australian Packed & Owned logo (attached or you can just use type), Please use Back Packaging copy attached. Please allow space for barcode, Batch number and expiry date.
Nice to have
• Vector background, natural earthy feel, natural or organic textures
• but we are open to any suggestions you might have.

```html
<!DOCTYPE html>
<html lang="en">
<head>
<meta charset="utf-8">
<title>Serenwell Calm Mix – Bath Soak Label</title>
<link rel="stylesheet" href="https://fonts.googleapis.com/css2?family=Dosis:wght@500;700&family=Open+Sans:wght@400;600&display=swap">
<style>
  :root {
    --canvas-bg: #ececec;
    --label-bg: #ffffff;
    --pattern-tint: #f4f3f5;
    --brand-purple: #5a2b87;
    --brand-magenta: #c3267f;
    --accent-pink: #e266a4;
    --ink-dark: #2b2b2b;
    --copy-grey: #b3b3b3;
    --white: #ffffff;
  }
  * { margin: 0; padding: 0; box-sizing: border-box; }
  html, body {
    width: 1200px;
    height: 1000px;
    overflow: hidden;
    background: var(--canvas-bg);
  }
  .canvas {
    position: relative;
    width: 1200px;
    height: 1000px;
  }
  .label {
    position: absolute;
    left: 310px;
    top: 82px;
    width: 580px;
    height: 836px;
    background: var(--label-bg);
    box-shadow: 0 2px 10px rgba(0,0,0,0.08);
    overflow: hidden;
  }
  .label__pattern {
    position: absolute;
    inset: 0;
    background: var(--pattern-tint);
  }
  .brand-box {
    position: absolute;
    left: 168px;
    top: 0;
    width: 232px;
    height: 326px;
    background: var(--label-bg);
    border-left: 3px solid var(--brand-purple);
    border-right: 3px solid var(--brand-purple);
    border-bottom: 3px solid var(--brand-purple);
    display: flex;
    flex-direction: column;
    align-items: center;
    padding-top: 96px;
  }
  .brand-box__name {
    font-family: "Open Sans", sans-serif;
    font-weight: 600;
    font-size: 50px;
    line-height: 1;
    color: var(--ink-dark);
    letter-spacing: 1px;
  }
  .brand-box__dot {
    margin-top: 38px;
    width: 56px;
    height: 56px;
    border-radius: 50%;
    background: var(--brand-magenta);
  }
  .product-type {
    position: absolute;
    left: 0;
    right: 0;
    top: 390px;
    text-align: center;
    font-family: "Dosis", sans-serif;
    font-weight: 500;
    font-size: 27px;
    letter-spacing: 3px;
    color: var(--accent-pink);
  }
  .name-band {
    position: absolute;
    left: 0;
    right: 0;
    top: 452px;
    height: 144px;
    background: linear-gradient(90deg, var(--brand-purple) 0%, #8a2a86 45%, var(--brand-magenta) 62%, var(--brand-purple) 100%);
    display: flex;
    flex-direction: column;
    align-items: center;
    justify-content: center;
    color: var(--white);
    font-family: "Dosis", sans-serif;
    font-weight: 700;
    text-align: center;
  }
  .name-band__title {
    font-size: 58px;
    line-height: 1;
    letter-spacing: 1px;
  }
  .name-band__subtitle {
    font-size: 27px;
    line-height: 1.2;
    margin-top: 6px;
    letter-spacing: 0.5px;
  }
  .description {
    position: absolute;
    left: 60px;
    right: 60px;
    top: 626px;
    text-align: center;
    font-family: "Open Sans", sans-serif;
    font-size: 17px;
    line-height: 1.5;
    color: var(--copy-grey);
  }
  .net-weight {
    position: absolute;
    left: 0;
    right: 0;
    top: 784px;
    text-align: center;
    font-family: "Open Sans", sans-serif;
    font-size: 17px;
    color: #9a9a9a;
  }
</style>
</head>
<body>
  <main class="canvas">
    <section class="label">
      <div class="label__pattern" role="img" aria-label="Faint grey floral line pattern covering the label background"></div>

      <div class="brand-box">
        <span class="brand-box__name">Lumora</span>
        <span class="brand-box__dot"></span>
      </div>

      <p class="product-type">BATH SOAK</p>

      <div class="name-band">
        <h1 class="name-band__title">SERENWELL</h1>
        <p class="name-band__subtitle">CALM MIX</p>
      </div>

      <p class="description">A unique blend of himalayan and magnesium flakes for the ultimate therapeutic bath soak. Our Serenwell Calm Mix will detoxify and revitalise your body.</p>

      <p class="net-weight">500grms</p>
    </section>
  </main>
</body>
</html>
```